Natural and organic skincare brand needs label design!

I need labels designed for my natural and organic skincare brand lumavale. The front of the bottles must contain the logo (image attached) and the following words: Formulated by a Naturopath; Anti-aging therapy; Organic Facial Oil; with CoEnzyme Q10 and Rosehip Seed Oil; 100ml e3.38fl.oz. Colours I would like used include black/white/grey/silver and aqua. I also like the grey woodgrain used on my draft website (check out www.lumavale-skin.com.au). The logo should be silver foil (shiny).The final design should be simple and communicate nature and sophistication. Some designs I like are found in the attachments. I intend to use black or white bottles.

Target Market(s)

women aged 30-50 interested in natural products

Industry/Entity Type

Skin Care Product

Font styles to use
Serif
Sans Serif
Decorative
Script
Other font styles liked:
• Any

Requirements
Must have
• Dimensions: 62mm (w) x 75mm (H) (front label only)
• Must contain the logo (image attached). The logo should be silver foil (shiny). and the following words are to be included on the label:
• Formulated by a Naturopath;
• Anti-aging Therapy;
• Organic Facial Oil;
• with CoEnzyme Q10 and Rosehip Seed Oil;
• 100ml e3.38fl.oz.
Nice to have
• Colours I would like used include black/white/grey/silver and aqua (turquoise). But I am also open to suggestion. I also like the grey woodgrain used on my draft website (check out www.lumavale-skin.com.au)

```html
<!DOCTYPE html>
<html lang="en">
<head>
<meta charset="utf-8">
<title>lumavale – Organic Facial Oil labels</title>
<link rel="stylesheet" href="https://fonts.googleapis.com/css2?family=Comfortaa:wght@300;400&family=Pinyon+Script&family=Tinos&family=Arimo:wght@400&display=swap">
<style>
  :root {
    --page: #ffffff;
    --ink-black: #0d0d0d;
    --ink-white: #f4f4f4;
    --paper-white: #f7f7f7;
    --silver-light: #e6e6e8;
    --silver-mid: #b9b9bd;
    --silver-dark: #8e8e93;
    --band-light: #d9d9db;
    --band-dark: #c4c4c6;
    --aqua: #8fd0c4;
    --text-dark: #2a2a2a;
  }
  * { margin: 0; padding: 0; box-sizing: border-box; }
  html, body { width: 1200px; height: 1182px; overflow: hidden; background: var(--page); }
  .sheet { position: relative; width: 1200px; height: 1182px; }

  .label {
    position: absolute;
    top: 277px;
    width: 520px;
    height: 628px;
    border-radius: 6px;
    overflow: hidden;
  }
  .label--black { left: 53px; background: var(--ink-black); color: var(--ink-white); }
  .label--white { left: 627px; background: var(--paper-white); color: var(--text-dark); border: 1px solid #e2e2e2; }

  .brand-seal {
    position: absolute;
    left: 185px; top: 60px;
    width: 150px; height: 150px;
    border-radius: 50%;
    background: radial-gradient(circle at 35% 30%, var(--silver-light), var(--silver-mid) 60%, var(--silver-dark));
    border: 3px solid var(--silver-light);
    display: flex; align-items: center; justify-content: center;
  }
  .brand-name {
    font-family: "Comfortaa", sans-serif;
    font-weight: 400;
    font-size: 24px;
    letter-spacing: 1px;
    color: #ffffff;
  }

  .botanical {
    position: absolute;
    left: 330px; top: 225px;
    width: 175px; height: 345px;
    border-radius: 40% 60% 30% 50%;
    background: radial-gradient(ellipse at 50% 40%, rgba(143,208,196,0.35), rgba(143,208,196,0.05) 70%, transparent);
  }

  .product-script {
    position: absolute;
    left: 62px; top: 278px;
    font-family: "Pinyon Script", cursive;
    font-size: 46px;
    line-height: 1;
  }
  .product-name {
    position: absolute;
    left: 56px; top: 318px;
    font-family: "Comfortaa", sans-serif;
    font-weight: 300;
    font-size: 80px;
    line-height: 1;
    letter-spacing: -1px;
  }
  .product-claim {
    position: absolute;
    left: 62px; top: 400px;
    font-family: "Comfortaa", sans-serif;
    font-weight: 300;
    font-size: 26px;
    line-height: 1;
  }
  .ingredient-band {
    position: absolute;
    left: 58px; top: 440px;
    width: 420px; height: 28px;
    display: flex; align-items: center;
    padding-left: 6px;
    font-family: "Arimo", sans-serif;
    font-size: 18px;
    color: var(--text-dark);
  }
  .label--black .ingredient-band { background: var(--band-dark); }
  .label--white .ingredient-band { background: var(--band-light); }
  .formulator {
    position: absolute;
    left: 62px; top: 478px;
    font-family: "Arimo", sans-serif;
    font-size: 17px;
  }
  .volume {
    position: absolute;
    left: 0; right: 0; top: 556px;
    text-align: center;
    font-family: "Tinos", serif;
    font-size: 17px;
  }
</style>
</head>
<body>
<main class="sheet">

  <section class="label label--black" aria-label="Front label on black">
    <div class="brand-seal"><span class="brand-name">lumavale</span></div>
    <div class="botanical" role="img" aria-label="Fine aqua line drawing of a rosehip branch with leaves and berries"></div>
    <p class="product-script">Organic</p>
    <h1 class="product-name">facial oil</h1>
    <p class="product-claim">anti-aging therapy</p>
    <p class="ingredient-band">with CoEnzyme Q10 and Rosehip Seed Oil</p>
    <p class="formulator">Formulated by a Naturopath</p>
    <p class="volume">100ml e3.38fl.oz.</p>
  </section>

  <section class="label label--white" aria-label="Front label on white">
    <div class="brand-seal"><span class="brand-name">lumavale</span></div>
    <div class="botanical" role="img" aria-label="Fine aqua line drawing of a rosehip branch with leaves and berries"></div>
    <p class="product-script">Organic</p>
    <h2 class="product-name">facial oil</h2>
    <p class="product-claim">anti-aging therapy</p>
    <p class="ingredient-band">with CoEnzyme Q10 and Rosehip Seed Oil</p>
    <p class="formulator">Formulated by a Naturopath</p>
    <p class="volume">100ml e3.38fl.oz.</p>
  </section>

</main>
</body>
</html>
```